Stationary Design needed for luxorious bespoke tailor

We need a design for our stationary items like businescards, letters, envelope and letter head / Signature for email. Our company "LE CORVAN" sells exclusively and luxourious bespoke garments and accessories for men. The desgins of letterhead, envelope and business card shoulderstand communicate luxury, high quality and good taste. We would like our logo to be used on the designs.

Target Market(s)

Gentleman with a high aproach and exclusive and luxourious suits and shirts, grooms, businesman,

Industry/Entity Type

It Company

Font styles to use
Sans Serif

Colors
ec1f27
ffffff

Requirements
Must have
• Logo, Companies name and adress, contactName internet & email, phone number line / mobile, VAT Nr. On Business Card frontpage only logo and name, adress companies on backpage. No VAT and Companies ID there. Company data; LE CORVAN AG Wiesenrain 42 4057 Basel Switzerland VAT: CHE 472 916 304 Tax Tel 41 61 594 17 36 Mobile 41 79 842 06 91 www.korvanmode.ch info@korvanmode.com.
Nice to have
• -Name And phone numbers need to be able to change (for different coworkers ...)
Should not have
• no VAT in Business Card

```html
<!DOCTYPE html>
<html lang="en">
<head>
<meta charset="utf-8">
<title>LE CORVAN – Business Card</title>
<link href="https://fonts.googleapis.com/css2?family=Roboto:wght@400;500&display=swap" rel="stylesheet">
<style>
  :root {
    --stage: #2f2f2f;
    --card-front: #ffffff;
    --card-back: #0f0b0b;
    --ink: #111111;
    --accent: #ec1f27;
    --muted: #8c8c8c;
    --rule: #4a4a4a;
  }
  * { margin: 0; padding: 0; box-sizing: border-box; }
  html, body { width: 1200px; height: 987px; overflow: hidden; }
  body {
    background: var(--stage);
    font-family: "Roboto", Arial, sans-serif;
    position: relative;
  }
  .card {
    position: absolute;
    width: 615px;
    height: 351px;
    box-shadow: 0 4px 10px rgba(0,0,0,0.45);
  }
  .card-front { left: 293px; top: 130px; background: var(--card-front); }
  .card-back { left: 292px; top: 505px; background: var(--card-back); }

  .brand-name {
    position: absolute;
    left: 0; right: 0; top: 148px;
    text-align: center;
    font-size: 46px;
    font-weight: 500;
    letter-spacing: 2px;
    color: var(--ink);
    line-height: 1;
  }

  .name-tab {
    position: absolute;
    left: 0; top: 142px;
    width: 14px; height: 43px;
    background: var(--accent);
  }
  .person-name {
    position: absolute;
    left: 43px; top: 140px;
    font-size: 21px;
    font-weight: 500;
    color: var(--muted);
    line-height: 1;
  }
  .person-role {
    position: absolute;
    left: 43px; top: 169px;
    font-size: 16px;
    color: var(--accent);
    line-height: 1;
  }
  .divider {
    position: absolute;
    left: 43px; top: 205px;
    width: 525px;
    border-top: 1px dashed var(--rule);
  }
  .contact-list {
    position: absolute;
    left: 43px; top: 220px;
    list-style: none;
  }
  .contact-list li {
    display: flex;
    align-items: center;
    height: 23.5px;
    font-size: 16px;
    color: var(--muted);
  }
  .contact-list svg {
    width: 15px; height: 15px;
    margin-right: 15px;
    fill: var(--muted);
    flex-shrink: 0;
  }
  .company-address {
    position: absolute;
    right: 47px; top: 224px;
    text-align: right;
    font-style: normal;
    font-size: 16px;
    line-height: 23.5px;
    color: var(--muted);
  }
</style>
</head>
<body>

<section class="card card-front">
  <div class="brand-name">LE CORVAN</div>
</section>

<section class="card card-back">
  <div class="name-tab"></div>
  <h1 class="person-name">ELIAS BRUNNER</h1>
  <p class="person-role">CEO/Founder</p>
  <div class="divider"></div>

  <ul class="contact-list">
    <li>
      <svg viewBox="0 0 16 16" aria-hidden="true"><path d="M3.2 1.5l2.3 2.6c.3.4.3.9 0 1.2L4.4 6.5c.8 1.9 2.4 3.6 4.4 4.6l1.2-1.1c.3-.3.9-.3 1.2 0l2.6 2.3c.4.3.4.9 0 1.3l-1.3 1.3c-.6.6-1.6.8-2.4.4C5.8 13.6 2.6 10.4 1 6.1.6 5.3.8 4.3 1.4 3.7l1.3-1.3c.2-.3.3-.9.5-.9z"/></svg>
      +41 61 594 17 36
    </li>
    <li>
      <svg viewBox="0 0 16 16" aria-hidden="true"><path d="M4.5 0h7c.8 0 1.5.7 1.5 1.5v13c0 .8-.7 1.5-1.5 1.5h-7C3.7 16 3 15.3 3 14.5v-13C3 .7 3.7 0 4.5 0zM5 2v10.5h6V2H5zm3 11.2a.9.9 0 100 1.8.9.9 0 000-1.8z"/></svg>
      +41 79 842 06 91
    </li>
    <li>
      <svg viewBox="0 0 16 16" aria-hidden="true"><path d="M1 3h14v1.2L8 8.6 1 4.2V3zm0 2.6l7 4.4 7-4.4V13H1V5.6z"/></svg>
      info@korvanmode.com
    </li>
    <li>
      <svg viewBox="0 0 16 16" aria-hidden="true"><path d="M8 1a7 7 0 100 14A7 7 0 008 1zm-1 2.2c.6.4.4 1.2-.2 1.5-.8.4-1.8.2-2 1.1-.2.8.8 1.1 1.4 1.5.7.5.4 1.5.9 2.1.4.6 1.3.5 1.4 1.3.1.7-.5 1.4-.3 2.1A5.6 5.6 0 012.4 8 5.6 5.6 0 017 3.2zm3.4.6a5.6 5.6 0 012.9 6.6c-.5-.3-.8-1-1.4-1.1-.8-.1-1.4.6-2.1.3-.8-.3-.5-1.5.1-2 .5-.4 1.4-.4 1.5-1.1.1-.6-.7-.9-.9-1.5-.1-.4-.1-.8-.1-1.2z"/></svg>
      www.korvanmode.com
    </li>
  </ul>

  <address class="company-address">
    LE CORVAN AG<br>
    Wiesenrain 42<br>
    4057 Basel<br>
    Switzerland
  </address>
</section>

</body>
</html>
```